Powerpoint Template Background Design

We are looking to update our powerpoint background to align better with our recently updated logo. I've included our current logo (BankGothic Md BT Medium) and previous ppt background we had used for reference. Page orientation should be landscape. Should be usable online and as a printable deck. We are in the digital advertising sales industry and represent various digital ad products to ad agencies and clients who are interested in marketing their products using mobile advertising tools. the RGB color yellow in our logo is 245, 191,34 #fsbf22. We like to also see the grey and black in our logo included. We'd like it to be similar but new and refreshed from our previous ppt background. I've added our current sales deck for your review and consideration with your design.

Target Market(s)

Advertisers, Ad agencies

Industry/Entity Type

Advertising

Colors
ffc214

Requirements
Must have
• Include Logo. Preferably our 3d logo on the cover page. color scheme should match our logo. Must have cover page and template border page that we will use throughout the entire presentation.
Nice to have
• Full cover page graphic using our 3d logo and allows us to add text in a fixed area of the slide
Should not have
• If recommending full slide color/imagery please note it will be used both online and as a printable deck. Do not include the tagline and/or text from the previously used presentation template.

```html
<!DOCTYPE html>
<html lang="en">
<head>
<meta charset="utf-8">
<title>Corvane Media – Presentation Template Overview</title>
<link rel="stylesheet" href="https://fonts.googleapis.com/css2?family=Open+Sans:wght@300;400;600;700;800&display=swap">
<style>
  :root{
    --canvas:#c8c8c8;
    --paper:#ffffff;
    --yellow:#f5bf22;
    --gold:#c99a0a;
    --olive:#9c7a00;
    --amber:#ffa000;
    --orange:#f7941d;
    --orange-deep:#e36c0a;
    --rust:#c85a00;
    --red:#d83a00;
    --red-deep:#b8250c;
    --ink:#222222;
    --grey:#8a8a8a;
    --grey-light:#d6d6d6;
    --text:#666666;
    --text-soft:#9a9a9a;
  }
  *{box-sizing:border-box;margin:0;padding:0}
  html,body{width:1200px;height:1200px;overflow:hidden;background:var(--canvas)}
  body{font-family:'Open Sans',Arial,sans-serif;color:var(--text)}
  .deck{
    display:grid;
    grid-template-columns:repeat(3,384px);
    grid-template-rows:repeat(5,216px);
    column-gap:8px;row-gap:20px;
    padding:27px 0 0 11px;
  }
  .slide{position:relative;background:var(--paper);overflow:hidden}
  .slide svg.art{position:absolute;left:0;top:0;width:384px;height:216px}
  .slide-title{position:absolute;top:20px;left:0;width:100%;text-align:center;font-weight:300;font-size:12.5px;color:var(--text)}
  .slide-title.left{text-align:left;left:35px}
  .slide-title strong{font-weight:600}
  .slide-sub{position:absolute;top:37px;left:0;width:100%;text-align:center;font-size:3.4px;color:#bbb}
  .slide-sub.left{text-align:left;left:35px}
  .dots{position:absolute;top:43px;left:0;width:100%;display:flex;justify-content:center;gap:1.3px}
  .dots.left{justify-content:flex-start;left:35px}
  .dots i{display:block;width:3.4px;height:3.4px;border-radius:50%;background:var(--yellow)}
  .dots i:nth-child(3){background:var(--grey)}
  .dots i:nth-child(4){background:var(--ink)}
  .page-no{position:absolute;right:9px;top:9px;width:11px;height:11px;border:.8px solid var(--yellow);border-radius:50%;font-size:4px;line-height:9.5px;text-align:center;color:var(--gold)}
  .brand{position:absolute;right:9px;bottom:8px;display:flex;align-items:center;gap:2px;font-weight:800;font-size:5px;letter-spacing:.8px;color:var(--ink)}
  .brand::before{content:"";width:5px;height:5px;border-radius:50%;background:var(--yellow)}
  .copy{position:absolute;font-size:3.6px;line-height:6.4px;color:var(--text-soft)}
  .copy p+p{margin-top:5px}
  .lead{color:var(--text);font-weight:600}

  .cover-brand{position:absolute;left:22px;top:40px;display:flex;align-items:center;gap:5px;font-weight:800;font-size:15px;line-height:15px;letter-spacing:3px;color:var(--ink)}
  .cover-brand::before{content:"";width:14px;height:14px;border-radius:50%;background:var(--yellow);flex:none}
  .cover-art{position:absolute;right:12px;top:6px;width:200px;height:170px;border-radius:50% 50% 40% 50%;background:radial-gradient(ellipse at 60% 45%,#f3e3b5 0%,#f6edd2 45%,#e3e3e3 75%,rgba(255,255,255,0) 76%)}
  .cover-title{position:absolute;left:22px;top:122px;font-weight:700;font-size:17.5px;color:var(--ink)}
  .cover-sub{position:absolute;left:22px;top:150px;font-size:5px;line-height:7.4px;color:var(--grey)}
  .cover-sub em{font-style:normal;color:var(--orange)}
  .cover-dots{position:absolute;left:22px;top:170px;display:flex;gap:1.3px}
  .cover-dots i{display:block;width:3.4px;height:3.4px;border-radius:50%;background:var(--yellow)}
  .cover-dots i:nth-child(3){background:var(--grey)}
  .cover-dots i:nth-child(4){background:var(--ink)}
  .cover-meta{position:absolute;left:22px;top:194px;font-size:4.6px;color:var(--grey)}
  .thanks{position:absolute;left:22px;top:108px;font-weight:800;font-size:24px;color:var(--ink)}
  .thanks-sub{position:absolute;left:22px;top:142px;font-weight:700;font-size:12px;color:var(--yellow)}

  .map-fill{position:absolute;background:linear-gradient(160deg,#e2e2e2,#cfcfcf);border-radius:30% 40% 35% 30%}

  .legend{position:absolute;font-size:3.8px;line-height:5.2px;color:var(--text-soft)}
  .legend li{list-style:none;position:relative;padding-left:8px;margin-bottom:6.4px}
  .legend li::before{content:"";position:absolute;left:0;top:.8px;width:3.6px;height:3.6px;border-radius:50%;background:var(--orange-deep)}
  .legend b{display:block;font-weight:400;font-size:4.2px;color:var(--orange-deep)}

  .pipe-list{position:absolute;left:212px;top:64px;width:150px;font-size:3.2px;line-height:4.3px;color:var(--text-soft)}
  .pipe-list div{margin-bottom:9.2px}
  .pipe-list b{display:block;font-weight:400;font-size:4.6px;line-height:6px;color:var(--orange)}

  .mission-col{position:absolute;top:136px;width:160px;font-size:3.4px;line-height:6.2px;color:var(--text-soft);text-align:center}
  .mission-col h3{font-size:6.2px;font-weight:700;color:#555;margin-bottom:4px}

  .note{position:absolute;font-size:3.2px;line-height:4.6px;color:var(--text-soft)}
  .note h4{font-size:5.4px;line-height:7px;font-weight:700;color:#555}
  .note.right-align{text-align:right}
  .session-end{position:absolute;top:169px;left:0;width:384px;text-align:center;font-size:9.5px;font-weight:400;color:#555}

  .timeline-head{position:absolute;right:22px;top:76px;text-align:right;font-size:10px;line-height:11px;font-weight:300;color:var(--grey)}
  .timeline-head strong{display:block;font-weight:600;font-size:13px;color:#555}
  .timeline-copy{position:absolute;right:22px;top:106px;width:70px;text-align:right;font-size:3.4px;line-height:7px;color:var(--text-soft)}
  .office{position:absolute;left:264px;top:80px;width:100px}
  .office h4{font-size:7.6px;font-weight:400;color:#555}
  .office .tag{font-size:4.2px;color:var(--grey);margin-bottom:8px}
  .office p{font-size:3.2px;line-height:7px;color:var(--text-soft)}
</style>
</head>
<body>
<main class="deck">

  <section class="slide cover">
    <div class="cover-art" role="img" aria-label="Large three-dimensional star logo graphic trailing a curved ribbon in yellow and grey tones"></div>
    <div class="cover-brand">CORVANE<br>MEDIA</div>
    <h1 class="cover-title">Presentation title goes here</h1>
    <p class="cover-sub">Multipurpose presentation for all <em>bussines</em> and<br><em>personal</em> powerpoint template</p>
    <div class="cover-dots"><i></i><i></i><i></i><i></i></div>
    <p class="cover-meta">Date / Presenter name</p>
  </section>

  <section class="slide">
    <h2 class="slide-title left">One Column Text</h2>
    <p class="slide-sub left">Put a relevant subtitle in this line</p>
    <div class="dots left"><i></i><i></i><i></i><i></i></div>
    <span class="page-no">10</span>
    <div class="copy" style="left:35px;top:84px;width:316px">
      <p class="lead" style="font-size:4.2px;margin-bottom:6px">Lorem Ipsum is not simply random text it has roots in a piece of classical Latin literature from 45 BC.</p>
      <p>There are many variations of passages of Lorem Ipsum available, but the majority have suffered alteration in some form, by injected humour, or randomised words which don't look even slightly believable. If you are going to use a passage of Lorem Ipsum, you need to be sure there isn't anything embarrassing hidden in the middle of text. There are many variations of passages of Lorem Ipsum available, but the majority have suffered alteration in some form, by injected humour, or randomised words which don't look even slightly believable. If you are going to use a passage of Lorem Ipsum, you need to be sure there isn't anything embarrassing hidden in the middle of text.</p>
      <p>The generated Lorem Ipsum is therefore always free from repetition, injected humour, or non-characteristic words. Contrary to popular belief it has roots in a piece of classical Latin literature from 45 BC. There are many variations of passages of Lorem Ipsum available, but the majority have suffered alteration in some form, by injected humour, or randomised words which don't look even slightly believable. If you are going to use a passage of Lorem Ipsum, you need to be sure there isn't anything embarrassing hidden in the middle of text.</p>
    </div>
    <div class="brand">CORVANE</div>
  </section>

  <section class="slide">
    <h2 class="slide-title">Two Column Text</h2>
    <p class="slide-sub">Put a relevant subtitle in this line</p>
    <div class="dots"><i></i><i></i><i></i><i></i></div>
    <span class="page-no">11</span>
    <div class="copy" style="left:35px;top:68px;width:154px;text-align:justify">
      <p class="lead" style="font-size:3.8px;margin-bottom:8px">It has roots in a piece of classical Latin literature from 45 BC.</p>
      <p>There are many variations of passages of Lorem Ipsum available, but the majority have suffered alteration in some form, by injected humour, or randomised words which don't look even slightly believable. If you are going to use a passage of Lorem Ipsum, you need to be sure there isn't anything embarrassing hidden in the middle of text. There are many variations of passages of Lorem Ipsum available, but the majority have suffered alteration in some form, by injected humour, or randomised words which don't look even slightly believable. If you are going to use a passage of Lorem Ipsum, you need to be sure there isn't anything embarrassing hidden in the middle of text.</p>
      <p>The generated Lorem Ipsum is therefore always free from repetition.</p>
    </div>
    <div class="copy" style="left:197px;top:68px;width:154px;text-align:justify">
      <p>Injected humour, or non characteristic words. Contrary to popular belief it has roots in a piece of classical Latin literature from 45 BC. There are many variations of passages of Lorem Ipsum available, but the majority have suffered alteration in some form, by injected humour, or randomised words which don't look even slightly believable. If you are going to use a passage of Lorem Ipsum, you need to be sure there isn't anything embarrassing hidden in the middle of text. There are many variations of passages of Lorem Ipsum available, but the majority have suffered alteration in some form, by injected humour, or randomised words which don't look even slightly believable. Contrary to popular belief it has roots in a piece of classical Latin literature from 45 BC.</p>
    </div>
    <div class="brand">CORVANE</div>
  </section>

  <section class="slide">
    <h2 class="slide-title">Snake Line Infographic</h2>
    <p class="slide-sub">Put a relevant subtitle in this line</p>
    <div class="dots"><i></i><i></i><i></i><i></i></div>
    <span class="page-no">19</span>
    <div class="copy" style="left:26px;top:80px;width:104px;line-height:6.4px">
      <p>The generated Lorem Ipsum is therefore always free from repetition, injected humour, or non characteristic words. Contrary to popular belief it has roots in a piece of classical Latin literature from 45 BC. There are many variations of passages of Lorem Ipsum available, but the majority have suffered alteration in some form, by injected humour, or randomised words which don't look even slightly believable.</p>
    </div>
    <svg class="art" viewBox="0 0 384 216" aria-hidden="true">
      <g font-size="3.6" fill="#f7941d">
        <text x="30" y="182">Cost</text><text x="46" y="182">Planning</text><text x="69" y="182">Sketch</text><text x="89" y="182">Brain</text><text x="105" y="182">Development</text>
      </g>
      <line x1="30" y1="185" x2="130" y2="185" stroke="#e0e0e0" stroke-width=".5"/>
      <g fill="none" stroke-width="15">
        <path d="M188,120 V140 A20,20 0 0 1 168,160" stroke="#222"/>
        <path d="M188,121 A20,20 0 0 1 228,121" stroke="#9c7a00"/>
        <path d="M228,119 A20,20 0 0 0 268,119" stroke="#c99a0a"/>
        <path d="M268,121 A20,20 0 0 1 308,121" stroke="#b85c00"/>
        <path d="M308,119 A20,20 0 0 0 348,119" stroke="#e07b00"/>
        <path d="M348,121 A20,20 0 0 1 388,121" stroke="#c62d0a"/>
      </g>
      <g fill="#fff">
        <circle cx="208" cy="100" r="4.5"/><circle cx="248" cy="140" r="4.5"/><circle cx="288" cy="100" r="4.5"/><circle cx="328" cy="140" r="4.5"/><circle cx="368" cy="100" r="4.5"/>
      </g>
      <g stroke="#fff" stroke-width="1">
        <circle cx="168" cy="163" r="6" fill="#222"/><circle cx="248" cy="157" r="6" fill="#c99a0a"/><circle cx="288" cy="83" r="6" fill="#b85c00"/><circle cx="328" cy="157" r="6" fill="#e07b00"/><circle cx="368" cy="83" r="6" fill="#c62d0a"/>
      </g>
      <g fill="#fff" font-size="4.4" font-weight="700" text-anchor="middle">
        <text x="168" y="164.6">01</text><text x="248" y="158.6">02</text><text x="288" y="84.6">03</text><text x="328" y="158.6">04</text><text x="368" y="84.6">05</text>
      </g>
    </svg>
    <div class="brand">CORVANE</div>
  </section>

  <section class="slide">
    <h2 class="slide-title">Design process Infographic</h2>
    <p class="slide-sub">Put a relevant subtitle in this line</p>
    <div class="dots"><i></i><i></i><i></i><i></i></div>
    <span class="page-no">21</span>
    <svg class="art" viewBox="0 0 384 216" aria-hidden="true">
      <g stroke="#d6d6d6" stroke-width=".4">
        <line x1="57" y1="73" x2="57" y2="100"/><line x1="113" y1="73" x2="113" y2="100"/><line x1="166" y1="73" x2="166" y2="100"/><line x1="203" y1="73" x2="203" y2="100"/><line x1="276" y1="73" x2="276" y2="100"/><line x1="329" y1="73" x2="329" y2="100"/>
        <line x1="40" y1="126" x2="40" y2="144"/><line x1="87" y1="126" x2="87" y2="144"/><line x1="145" y1="128" x2="145" y2="144"/><line x1="186" y1="124" x2="186" y2="144"/><line x1="243" y1="134" x2="243" y2="144"/><line x1="305" y1="126" x2="305" y2="144"/><line x1="343" y1="120" x2="343" y2="144"/>
      </g>
      <circle cx="40" cy="110" r="16" fill="#c99a0a"/>
      <circle cx="68" cy="110" r="14" fill="#d9a800"/>
      <circle cx="92" cy="110" r="12" fill="#e6b400"/>
      <circle cx="113" cy="110" r="20" fill="#ffa000"/>
      <circle cx="145" cy="110" r="17" fill="#ffae1a"/>
      <circle cx="173" cy="110" r="11" fill="#e39000"/>
      <circle cx="189" cy="110" r="9" fill="#c56a00"/>
      <circle cx="203" cy="110" r="6" fill="#e07b00"/>
      <circle cx="243" cy="110" r="23" fill="#ff8a00"/>
      <circle cx="276" cy="110" r="14" fill="#ff6f00"/>
      <circle cx="305" cy="110" r="13" fill="#ff4a00"/>
      <circle cx="325" cy="110" r="6" fill="#f23a00"/>
      <circle cx="343" cy="110" r="7" fill="#e0330a"/>
      <g fill="#fff">
        <circle cx="40" cy="110" r="4"/><circle cx="113" cy="110" r="4"/><circle cx="186" cy="110" r="3"/><circle cx="243" cy="110" r="4"/>
      </g>
      <path d="M300,110 l3,3 l6,-6" stroke="#fff" stroke-width="1.6" fill="none"/>
      <path d="M340,113 l6,-6 M342,107 h4 v4" stroke="#fff" stroke-width="1" fill="none"/>
      <g font-size="3.8" fill="#888" text-anchor="middle">
        <text x="57" y="70">Data Analysis</text><text x="113" y="70">Sketch</text><text x="166" y="70">Client Revision</text><text x="203" y="70">Fixes</text><text x="276" y="70">Meet up</text><text x="329" y="70">Revise</text>
        <text x="40" y="149">Project Brief</text><text x="87" y="149">Research</text><text x="145" y="149">Proposals</text><text x="186" y="149">Improvements</text><text x="243" y="149">Proposal</text><text x="305" y="149">Fixes</text><text x="343" y="149">Launch</text>
      </g>
      <line x1="25" y1="178" x2="360" y2="178" stroke="#e6e6e6" stroke-width=".5"/>
      <g font-size="3" fill="#aaa">
        <circle cx="56" cy="183" r="1.5" fill="#9c7a00"/><text x="59" y="184">Meet</text>
        <circle cx="99" cy="183" r="1.5" fill="#e6b400"/><text x="102" y="184">Development</text>
        <circle cx="154" cy="183" r="1.5" fill="#e39000"/><text x="157" y="184">Revisions</text>
        <circle cx="203" cy="183" r="1.5" fill="#ff8a00"/><text x="206" y="184">Client Review</text>
        <circle cx="256" cy="183" r="1.5" fill="#ff4a00"/><text x="259" y="184">Fixes</text>
        <circle cx="290" cy="183" r="1.5" fill="#e0330a"/><text x="293" y="184">Project Launch</text>
      </g>
    </svg>
    <div class="brand">CORVANE</div>
  </section>

  <section class="slide">
    <h2 class="slide-title"><strong>HELLO</strong> Arround the World</h2>
    <p class="slide-sub">Put a relevant subtitle in this line</p>
    <div class="dots"><i></i><i></i><i></i><i></i></div>
    <span class="page-no">6</span>
    <div class="map-fill" style="left:22px;top:70px;width:230px;height:104px" role="img" aria-label="World map in light grey with highlighted regions in orange for the United States, Brazil, Russia, China and Australia"></div>
    <p style="position:absolute;left:97px;top:178px;font-size:3.8px;color:#999"><b style="color:#555">Something</b> about me that you should know</p>
    <ul class="legend" style="left:256px;top:72px;width:110px">
      <li><b>United State (Washington DC)</b>Lorem ipsum dolor sit amet, consectetur adipiscing elit.</li>
      <li><b>North America (Brazil)</b>Lorem ipsum dolor sit amet, consectetur adipiscing elit.</li>
      <li><b>Europe (Russia)</b>Lorem ipsum dolor sit amet, consectetur adipiscing elit.</li>
      <li><b>Asia (China)</b>Lorem ipsum dolor sit amet, consectetur adipiscing elit.</li>
      <li><b>Australia (Queensland)</b>Lorem ipsum dolor sit amet, consectetur adipiscing elit.</li>
    </ul>
    <div class="brand">CORVANE</div>
  </section>

  <section class="slide">
    <h2 class="slide-title">Work with Social Media</h2>
    <p class="slide-sub">Put a relevant subtitle in this line</p>
    <div class="dots"><i></i><i></i><i></i><i></i></div>
    <span class="page-no">13</span>
    <svg class="art" viewBox="0 0 384 216" aria-hidden="true">
      <g stroke-dasharray="1.5 1" stroke-width=".5">
        <line x1="78" y1="70" x2="78" y2="100" stroke="#c99a0a"/><line x1="110" y1="70" x2="110" y2="94" stroke="#ffa000"/><line x1="147" y1="70" x2="147" y2="88" stroke="#c85a00"/><line x1="183" y1="70" x2="183" y2="106" stroke="#ff8a00"/><line x1="219" y1="70" x2="219" y2="100" stroke="#ff4a00"/><line x1="255" y1="70" x2="255" y2="108" stroke="#c62d0a"/><line x1="286" y1="70" x2="286" y2="112" stroke="#222"/>
      </g>
      <g>
        <circle cx="78" cy="66" r="2.5" fill="#c99a0a"/><circle cx="110" cy="66" r="2.5" fill="#ffa000"/><circle cx="147" cy="66" r="2.5" fill="#c85a00"/><circle cx="183" cy="66" r="2.5" fill="#ff8a00"/><circle cx="219" cy="66" r="2.5" fill="#ff4a00"/><circle cx="255" cy="66" r="2.5" fill="#c62d0a"/><circle cx="286" cy="66" r="2.5" fill="#222"/>
      </g>
      <path d="M48,141 C66,141 70,100 78,100 C86,100 90,141 108,141Z" fill="#c99a0a"/>
      <path d="M80,141 C98,141 102,94 110,94 C118,94 122,141 140,141Z" fill="#ffa000"/>
      <path d="M117,141 C135,141 139,88 147,88 C155,88 159,141 177,141Z" fill="#c85a00"/>
      <path d="M153,141 C171,141 175,106 183,106 C191,106 195,141 213,141Z" fill="#ff8a00"/>
      <path d="M189,141 C207,141 211,100 219,100 C227,100 231,141 249,141Z" fill="#ff4a00"/>
      <path d="M225,141 C243,141 247,108 255,108 C263,108 267,141 285,141Z" fill="#c62d0a"/>
      <path d="M256,141 C274,141 278,112 286,112 C294,112 298,141 316,141Z" fill="#222"/>
      <g font-size="4" font-weight="700" fill="#fff" text-anchor="middle">
        <text x="78" y="137">20%</text><text x="110" y="137">40%</text><text x="147" y="137">62%</text><text x="183" y="137">35%</text><text x="219" y="137">50%</text><text x="255" y="137">24%</text><text x="286" y="137">18%</text>
      </g>
      <g font-size="3.6" fill="#888" text-anchor="middle">
        <text x="78" y="155">Pagebook</text><text x="110" y="155">Linkline</text><text x="147" y="155">Searchly</text><text x="183" y="155">Pinboard</text><text x="219" y="155">Chirper</text><text x="255" y="155">Viewtube</text><text x="286" y="155">Snapstream</text>
      </g>
    </svg>
    <div class="copy" style="left:40px;top:166px;width:304px;text-align:center">
      <p>There are many variations of passages of Lorem Ipsum available, but the majority have suffered alteration in some form, by injected humour, or randomised words which don't look even slightly believable. If you are going to use a passage of Lorem Ipsum, you need to be sure there isn't anything embarrassing hidden in the middle of text.</p>
    </div>
    <div class="brand">CORVANE</div>
  </section>

  <section class="slide">
    <h2 class="slide-title">Stacked Venn</h2>
    <p class="slide-sub">Put a relevant subtitle in this line</p>
    <div class="dots"><i></i><i></i><i></i><i></i></div>
    <span class="page-no">14</span>
    <svg class="art" viewBox="0 0 384 216" aria-hidden="true">
      <g stroke-dasharray="1.5 1.2" stroke-width=".5" fill="none">
        <line x1="106" y1="64" x2="280" y2="64" stroke="#c99a0a"/>
        <line x1="90" y1="88" x2="294" y2="88" stroke="#ff7a00"/>
        <line x1="78" y1="113" x2="300" y2="113" stroke="#c85a00"/>
        <line x1="98" y1="152" x2="280" y2="152" stroke="#ffa000"/>
      </g>
      <circle cx="192" cy="125" r="64" fill="#c99a0a"/>
      <circle cx="192" cy="141" r="48" fill="#ff7a00"/>
      <circle cx="192" cy="151" r="38" fill="#c85a00"/>
      <circle cx="192" cy="163" r="26" fill="#ffa000"/>
      <g font-size="5" font-weight="700" fill="#fff" text-anchor="middle">
        <text x="192" y="83">30%</text><text x="192" y="108">26%</text><text x="192" y="133">24%</text><text x="192" y="168">20%</text>
      </g>
      <g>
        <circle cx="96" cy="64" r="3.6" fill="#c99a0a"/><circle cx="82" cy="88" r="3.6" fill="#ff7a00"/><circle cx="70" cy="113" r="3.6" fill="#c85a00"/><circle cx="90" cy="152" r="3.6" fill="#ffa000"/>
        <circle cx="280" cy="64" r="1.4" fill="#c99a0a"/><circle cx="294" cy="88" r="1.4" fill="#ff7a00"/><circle cx="300" cy="113" r="1.4" fill="#c85a00"/><circle cx="280" cy="152" r="1.4" fill="#ffa000"/>
      </g>
      <g font-size="3.8" font-weight="600" fill="#555">
        <text x="285" y="65">Searchly</text><text x="298" y="89">Chirper</text><text x="306" y="114">Linkline</text><text x="285" y="153">Pinboard</text>
      </g>
      <g font-size="3" fill="#aaa">
        <text x="285" y="70">Lorem ipsum dolor sit amet</text><text x="285" y="74">consectetur sagittis purus</text>
        <text x="298" y="94">Lorem ipsum dolor sit amet</text><text x="298" y="98">consectetur sagittis purus</text>
        <text x="306" y="119">Lorem ipsum dolor sit amet</text><text x="306" y="123">consectetur sagittis purus</text>
        <text x="285" y="158">Lorem ipsum dolor sit amet</text><text x="285" y="162">consectetur sagittis purus</text>
      </g>
    </svg>
    <div class="brand">CORVANE</div>
  </section>

  <section class="slide">
    <h2 class="slide-title">Pipe Line Infographic</h2>
    <p class="slide-sub">Put a relevant subtitle in this line</p>
    <div class="dots"><i></i><i></i><i></i><i></i></div>
    <span class="page-no">20</span>
    <svg class="art" viewBox="0 0 384 216" aria-hidden="true">
      <g>
        <path d="M80,74 H130 V92 H75 L70,83Z" fill="#9c7a00"/>
        <rect x="130" y="68" width="30" height="22" fill="#d9a800"/><path d="M130,68 l8,-5 h30 l-8,5Z" fill="#f5c430"/><path d="M160,68 l8,-5 v22 l-8,5Z" fill="#b58a00"/>
        <path d="M65,94 H122 V112 H60 L56,103Z" fill="#c99a0a"/>
        <rect x="122" y="90" width="38" height="22" fill="#ffa000"/><path d="M160,90 l8,-5 v22 l-8,5Z" fill="#d98800"/>
        <path d="M46,114 H112 V132 H40 L36,123Z" fill="#b85c00"/>
        <rect x="112" y="112" width="48" height="22" fill="#e07b00"/><path d="M160,112 l8,-5 v22 l-8,5Z" fill="#b85c00"/>
        <path d="M62,136 H122 V154 H56 L52,145Z" fill="#e36c0a"/>
        <rect x="122" y="134" width="38" height="22" fill="#ff6a00"/><path d="M160,134 l8,-5 v22 l-8,5Z" fill="#cc5000"/>
        <path d="M76,158 H130 V176 H70 L66,167Z" fill="#c62d0a"/>
        <rect x="130" y="156" width="30" height="22" fill="#e0330a"/><path d="M160,156 l8,-5 v22 l-8,5Z" fill="#a82000"/>
      </g>
      <g fill="#fff" font-size="3.2" font-weight="700" text-anchor="middle">
        <text x="103" y="80">Content 01</text><text x="93" y="100">Content 02</text><text x="80" y="120">Content 03</text><text x="93" y="142">Content 04</text><text x="103" y="164">Content 05</text>
      </g>
      <g fill="#fff" font-size="2.4" text-anchor="middle">
        <text x="103" y="85">Suitable for all category,</text><text x="103" y="89">Lorem Ipsum is not simply</text>
        <text x="93" y="105">Suitable for all category,</text><text x="93" y="109">Lorem Ipsum is not simply</text>
        <text x="80" y="125">Suitable for all category,</text><text x="80" y="129">Lorem Ipsum is not simply</text>
        <text x="93" y="147">Suitable for all category,</text><text x="93" y="151">Lorem Ipsum is not simply</text>
        <text x="103" y="169">Suitable for all category,</text><text x="103" y="173">Lorem Ipsum is not simply</text>
      </g>
      <g fill="none" stroke="#fff" stroke-width=".8">
        <rect x="140" y="74" width="8" height="6"/><path d="M137,100 h10 l-5,5z"/><rect x="132" y="118" width="10" height="7" rx="1"/><path d="M138,142 l5,-5 l4,4 l-5,5z"/><path d="M142,170 l6,-6 l2,2 l-6,6z"/>
      </g>
    </svg>
    <div class="pipe-list">
      <div><b>Delivery</b>Curabitur a nisl facilisis lectus posuere pharetra porta sed neque. Fusce porttitor venenatis ipsum ut ullamcorper.</div>
      <div><b>Premium Packages</b>Curabitur a nisl facilisis lectus posuere pharetra porta sed neque. Fusce porttitor venenatis ipsum ut ullamcorper.</div>
      <div><b>Concept</b>Curabitur a nisl facilisis lectus posuere pharetra porta sed neque. Fusce porttitor venenatis ipsum ut ullamcorper.</div>
      <div><b>More Expensive</b>Curabitur a nisl facilisis lectus posuere pharetra porta sed neque. Fusce porttitor venenatis ipsum ut ullamcorper.</div>
      <div><b>Editable</b>Curabitur a nisl facilisis lectus posuere pharetra porta sed neque. Fusce porttitor venenatis ipsum ut ullamcorper.</div>
    </div>
    <div class="brand">CORVANE</div>
  </section>

  <section class="slide">
    <h2 class="slide-title">Vision and Mission</h2>
    <p class="slide-sub">Put a relevant subtitle in this line</p>
    <div class="dots"><i></i><i></i><i></i><i></i></div>
    <span class="page-no">7</span>
    <svg class="art" viewBox="0 0 384 216" aria-hidden="true">
      <g stroke="#eee" stroke-width="1.4">
        <circle cx="71" cy="85" r="13" fill="#ffa000"/><circle cx="131" cy="85" r="13" fill="#c85a00"/><circle cx="193" cy="85" r="13" fill="#ff7a00"/><circle cx="254" cy="85" r="13" fill="#ff4a00"/><circle cx="314" cy="85" r="13" fill="#d83a00"/>
      </g>
      <g fill="none" stroke="#fff" stroke-width=".9">
        <path d="M66,89 h10 a3,3 0 0 0 0,-6 a4,4 0 0 0 -8,-1 a3,3 0 0 0 -2,7z"/>
        <rect x="126" y="81" width="10" height="8" rx="1"/>
        <path d="M193,91 l-5,-5 a3,3 0 0 1 5,-4 a3,3 0 0 1 5,4z"/>
        <path d="M250,90 l7,-7 l2,2 l-7,7 h-2z"/>
        <circle cx="314" cy="85" r="4"/><circle cx="314" cy="85" r="1.5"/>
      </g>
      <g font-size="4.2" fill="#e07b00" text-anchor="middle">
        <text x="71" y="108">Downloading</text><text x="131" y="108">Presentation</text><text x="193" y="108">Lovely</text><text x="254" y="108">Editable</text><text x="314" y="108">Improvement</text>
      </g>
      <line x1="34" y1="124" x2="362" y2="124" stroke="#e6e6e6" stroke-width=".6"/>
    </svg>
    <div class="mission-col" style="left:30px"><h3 style="text-align:right;padding-right:4px">Company Vision</h3>It was popularised in the 1960s with the release of Typesheet transfer sheets containing Lorem Ipsum passages, and more recently with desktop publishing software like PageComposer including versions of Lorem Ipsum. when an unknown printer took a galley of type and scrambled it to make a type specimen book. It has survived not only five centuries, but also the leap into electronic typesetting.</div>
    <div class="mission-col" style="left:204px;text-align:left"><h3>Company Mission</h3>It was popularised in the 1960s with the release of Typesheet transfer sheets containing Lorem Ipsum passages, and more recently with desktop publishing software like PageComposer including versions of Lorem Ipsum. when an unknown printer took a galley of type and scrambled it to make a type specimen book. It has survived not only five centuries, but also the leap into electronic typesetting.</div>
    <div class="brand">CORVANE</div>
  </section>

  <section class="slide">
    <h2 class="slide-title">Presentation Session</h2>
    <p class="slide-sub">Put a relevant subtitle in this line</p>
    <div class="dots"><i></i><i></i><i></i><i></i></div>
    <span class="page-no">2</span>
    <svg class="art" viewBox="0 0 384 216" aria-hidden="true">
      <circle cx="193" cy="64" r="1.4" fill="#222"/>
      <line x1="193" y1="64" x2="193" y2="140" stroke="#222" stroke-width=".7" stroke-dasharray="2 1.4"/>
      <line x1="193" y1="140" x2="193" y2="216" stroke="#f5bf22" stroke-width=".7"/>
      <circle cx="193" cy="112" r="1.4" fill="#888"/><circle cx="193" cy="161" r="1.4" fill="#f5bf22"/>
      <g transform="translate(170 112) rotate(45)"><rect x="-10" y="-10" width="20" height="20" fill="none" stroke="#888" stroke-width="2"/><rect x="-7" y="-7" width="14" height="14" fill="#fff"/></g>
      <path d="M168,108 h4 v6 h-4z M170,114 v3" stroke="#888" stroke-width=".7" fill="none"/>
      <g transform="translate(214 161) rotate(45)"><rect x="-10" y="-10" width="20" height="20" fill="none" stroke="#f5bf22" stroke-width="2"/><rect x="-7" y="-7" width="14" height="14" fill="#fbe2a0"/></g>
      <circle cx="214" cy="161" r="3.4" fill="none" stroke="#f5bf22" stroke-width=".8"/>
    </svg>
    <div class="note right-align" style="left:80px;top:100px;width:74px"><h4 style="font-size:5.6px">Opening</h4>When an unknown printer took a galley of type and scrambled it to make a type specimen book.</div>
    <div class="note" style="left:236px;top:150px;width:74px"><h4 style="font-size:5.6px">Meet the Team</h4>When an unknown printer took a galley of type and scrambled it to make a type specimen book.</div>
    <div class="brand">CORVANE</div>
  </section>

  <section class="slide">
    <span class="page-no">3</span>
    <svg class="art" viewBox="0 0 384 216" aria-hidden="true">
      <line x1="193" y1="0" x2="193" y2="52" stroke="#f5bf22" stroke-width=".7"/>
      <line x1="193" y1="52" x2="193" y2="128" stroke="#222" stroke-width=".7" stroke-dasharray="2 1.4"/>
      <line x1="193" y1="128" x2="193" y2="162" stroke="#888" stroke-width=".7"/>
      <circle cx="193" cy="52" r="1.4" fill="#f5bf22"/><circle cx="193" cy="88" r="1.4" fill="#222"/><circle cx="193" cy="126" r="1.4" fill="#888"/>
      <g transform="translate(171 51) rotate(45)"><rect x="-10" y="-10" width="20" height="20" fill="none" stroke="#f5bf22" stroke-width="2"/><rect x="-7" y="-7" width="14" height="14" fill="#fbe2a0"/></g>
      <circle cx="171" cy="51" r="3.4" fill="none" stroke="#f5bf22" stroke-width=".9"/>
      <g transform="translate(215 88) rotate(45)"><rect x="-10" y="-10" width="20" height="20" fill="none" stroke="#222" stroke-width="2"/><rect x="-7" y="-7" width="14" height="14" fill="#fff"/></g>
      <rect x="211" y="85" width="8" height="6" fill="none" stroke="#222" stroke-width=".8"/>
      <g transform="translate(171 126) rotate(45)"><rect x="-10" y="-10" width="20" height="20" fill="none" stroke="#888" stroke-width="2"/><rect x="-7" y="-7" width="14" height="14" fill="#fff"/></g>
      <path d="M167,128 l8,-5 l-3,8 l-1,-3z" fill="none" stroke="#888" stroke-width=".7"/>
    </svg>
    <div class="note right-align" style="left:76px;top:43px;width:78px"><h4>Map and Social Media</h4>When an unknown printer took a galley of type and scrambled it to make a type specimen book.</div>
    <div class="note" style="left:237px;top:80px;width:74px"><h4>Portfolio Sample</h4>When an unknown printer took a galley of type and scrambled it to make a type specimen book.</div>
    <div class="note right-align" style="left:76px;top:117px;width:78px"><h4>Closing</h4>When an unknown printer took a galley of type and scrambled it to make a type specimen book.</div>
    <p class="session-end">SESSION END</p>
    <div class="brand">CORVANE</div>
  </section>

  <section class="slide">
    <span class="page-no">4</span>
    <svg class="art" viewBox="0 0 384 216" aria-hidden="true">
      <path d="M40,176 V158 H66 V136 H86 V108 H104 V96 H130 V120 H155 V104 H177 V92 H196 V70 H208 V60 H237" fill="none" stroke="#f5bf22" stroke-width="6" stroke-linejoin="round"/>
      <path d="M86,136 V108 H104 V96 H130 V120 H155" fill="none" stroke="#ffa000" stroke-width="6" stroke-linejoin="round"/>
      <path d="M155,120 V104 H177 V92 H196 V70 H208 V60 H237" fill="none" stroke="#ff6a00" stroke-width="6" stroke-linejoin="round"/>
      <path d="M196,70 H208 V60 H237" fill="none" stroke="#e0330a" stroke-width="6" stroke-linejoin="round"/>
      <circle cx="40" cy="176" r="11" fill="#fff" stroke="#f5bf22" stroke-width="3"/>
      <text x="40" y="178" font-size="6.4" font-weight="800" fill="#222" text-anchor="middle">GO</text>
      <g fill="#fff" stroke-width="2.4">
        <circle cx="70" cy="136" r="8" stroke="#f5bf22"/><circle cx="107" cy="96" r="8" stroke="#ffa000"/><circle cx="143" cy="120" r="8" stroke="#ffa000"/><circle cx="177" cy="104" r="8" stroke="#ff6a00"/><circle cx="237" cy="59" r="11" stroke="#e0330a"/>
      </g>
      <g fill="#f5bf22"><circle cx="70" cy="136" r="3"/><circle cx="107" cy="96" r="3"/><circle cx="143" cy="120" r="3" fill="#c85a00"/><circle cx="177" cy="104" r="3" fill="#ff6a00"/><circle cx="237" cy="59" r="5" fill="#e0330a"/></g>
      <g font-size="4.2" font-weight="700" fill="#e07b00" text-anchor="middle">
        <text x="71" y="124">2002</text><text x="107" y="84">2006</text><text x="144" y="109">2010</text><text x="180" y="93">2014</text><text x="211" y="56">2018</text>
      </g>
      <text x="256" y="57" font-size="4.2" font-weight="700" fill="#222">TURN GLOBAL</text>
      <g font-size="3.8" font-weight="700" fill="#222" text-anchor="middle">
        <text x="46" y="132">We Born</text><text x="79" y="93">We Growth</text><text x="144" y="149">We Thrive</text><text x="184" y="129">We Stronger</text><text x="231" y="84">Unbelivable</text>
      </g>
      <g font-size="3" fill="#aaa" text-anchor="middle">
        <text x="46" y="137">Lorem ipsum</text><text x="46" y="141">dolor sit amet</text><text x="46" y="145">connec tetur</text>
        <text x="79" y="98">Lorem ipsum</text><text x="79" y="102">dolor sit amet</text><text x="79" y="106">connec tetur</text>
        <text x="144" y="154">Lorem ipsum</text><text x="144" y="158">dolor sit amet</text><text x="144" y="162">connec tetur</text>
        <text x="184" y="134">Lorem ipsum</text><text x="184" y="138">dolor sit amet</text><text x="184" y="142">connec tetur</text>
        <text x="231" y="89">Lorem ipsum</text><text x="231" y="93">dolor sit amet</text><text x="231" y="97">connec tetur</text>
      </g>
    </svg>
    <h2 class="timeline-head">COMPANY<strong>TIMELINE</strong></h2>
    <p class="timeline-copy">Suitable for all categories business and personal presentation, eaque ipsa quae ab illo inventore veritatis et quasi architecto beatae vitae dicta sunt explicabo. Suitable for all categories business and personal presentation.</p>
    <div class="brand">CORVANE</div>
  </section>

  <section class="slide">
    <h2 class="slide-title">World Map</h2>
    <p class="slide-sub">Put a relevant subtitle in this line</p>
    <div class="dots"><i></i><i></i><i></i><i></i></div>
    <span class="page-no">5</span>
    <div class="map-fill" style="left:26px;top:70px;width:190px;height:100px" role="img" aria-label="World map in light grey with the United States highlighted in orange and a dotted leader to an office marker"></div>
    <svg class="art" viewBox="0 0 384 216" aria-hidden="true">
      <path d="M60,113 V176 H104" fill="none" stroke="#f5bf22" stroke-width=".5" stroke-dasharray="1.4 1"/>
      <circle cx="104" cy="176" r="4" fill="#fff" stroke="#e07b00" stroke-width=".8"/><circle cx="104" cy="176" r="1.6" fill="#e07b00"/>
      <text x="115" y="174" font-size="4" fill="#555">HELLO</text>
      <text x="115" y="179" font-size="2.8" fill="#aaa">1001 Harbour Crescent, Lindenfield, PA 55102</text>
      <text x="115" y="183" font-size="2.8" fill="#aaa">Northwind · USA</text>
    </svg>
    <div class="office">
      <h4>Office Location</h4>
      <p class="tag">Something about me that you should know</p>
      <p>Suitable for all categories business and personal presentation, eaque ipsa quae ab illo inventore veritatis et quasi architecto beatae vitae dicta sunt explicabo. Suitable for all categories business and personal presentation, eaque ipsa quae ab illo inventore veritatis et quasi architecto beatae vitae dicta sunt explicabo.</p>
    </div>
    <div class="brand">CORVANE</div>
  </section>

  <section class="slide cover">
    <div class="cover-art" role="img" aria-label="Large three-dimensional star logo graphic trailing a curved ribbon in yellow and grey tones"></div>
    <div class="cover-brand" style="top:30px">CORVANE<br>MEDIA</div>
    <p class="thanks">THANKS</p>
    <p class="thanks-sub">FOR WATCHING</p>
  </section>

</main>
</body>
</html>
```